Night Dresses business cards business requirers

We are a new company initiating Mexico operations. Our core business is Night woman dress (both formal and party dress) for rent. Gownhaven is the name of the company. ITS Gownhaven form by two word. The dress word and topia (Utopic) so the place Gownhaven Means That You cant get the ideal, perfect and unique dress for your event. So we would like a modern, very creative, and attractive business card.

Industry/Entity Type

Womens Clothing

Contact Information for Business Card

Rounded Borders, two faces

Requirements
Must have
• Rounded borders, logo and slogan, modern, glam, attractive design
Should not have
• modern design classic or not

```html
<!DOCTYPE html>
<html lang="en">
<head>
<meta charset="utf-8">
<title>Gownhaven Business Card</title>
<link rel="stylesheet" href="https://fonts.googleapis.com/css2?family=PT+Sans+Narrow:wght@400;700&display=swap">
<style>
  :root {
    --bg: #e6e4e6;
    --plum: #a5578a;
    --card-white: #f3f3f3;
    --band-grey: #5c5c5c;
    --ink-grey: #565656;
    --ink-dark: #3a3a3a;
  }
  html, body {
    margin: 0;
    padding: 0;
    width: 1200px;
    height: 1197px;
    overflow: hidden;
    background: var(--bg);
  }
  .sheet {
    position: relative;
    width: 1200px;
    height: 1197px;
  }
  .card {
    position: absolute;
    left: 170px;
    width: 860px;
    height: 518px;
    border-radius: 24px;
    overflow: hidden;
    background: var(--card-white);
    box-shadow: 0 6px 18px rgba(0,0,0,0.18);
  }
  .card--front { top: 50px; }
  .card--back { top: 629px; }
  .card-shapes {
    position: absolute;
    inset: 0;
    width: 100%;
    height: 100%;
  }
  .shape-plum { fill: var(--plum); }
  .shape-band { fill: var(--band-grey); }

  .brand {
    position: absolute;
    display: flex;
    align-items: center;
    gap: 14px;
    transform: translate(-50%, -50%);
  }
  .brand-dot {
    flex: none;
    border-radius: 50%;
    background: var(--ink-grey);
  }
  .brand-name {
    font-family: "PT Sans Narrow", sans-serif;
    font-weight: 400;
    color: var(--ink-grey);
    white-space: nowrap;
    line-height: 1;
  }

  .card--front .brand { left: 378px; top: 280px; }
  .card--front .brand-dot { width: 22px; height: 22px; }
  .card--front .brand-name { font-size: 58px; letter-spacing: 4px; }

  .card--back .brand { left: 203px; top: 170px; }
  .card--back .brand-dot { width: 17px; height: 17px; }
  .card--back .brand-name { font-size: 44px; letter-spacing: 3px; }

  .holder {
    position: absolute;
    left: 64px;
    top: 338px;
    font-family: "PT Sans Narrow", sans-serif;
  }
  .holder-name {
    font-weight: 700;
    font-size: 30px;
    color: var(--plum);
    line-height: 1;
  }
  .holder-role {
    font-size: 22px;
    color: var(--ink-dark);
    line-height: 1.1;
  }

  .contact-list {
    position: absolute;
    left: 290px;
    top: 298px;
    margin: 0;
    padding: 0;
    list-style: none;
    font-family: "PT Sans Narrow", sans-serif;
    font-size: 24px;
    color: var(--plum);
  }
  .contact-item {
    display: flex;
    align-items: center;
    gap: 14px;
    height: 35px;
  }
  .contact-icon {
    width: 18px;
    height: 18px;
    fill: var(--ink-dark);
    flex: none;
  }
</style>
</head>
<body>
<main class="sheet">

  <section class="card card--front" aria-label="Business card front">
    <svg class="card-shapes" viewBox="0 0 435 262" preserveAspectRatio="none" aria-hidden="true">
      <polygon class="shape-plum" points="0,0 157,0 12,237 0,237"/>
      <rect class="shape-band" x="0" y="237" width="300" height="10"/>
      <polygon class="shape-plum" points="408,0 435,0 435,262 273,262"/>
    </svg>
    <div class="brand">
      <div class="brand-dot"></div>
      <div class="brand-name">GOWNHAVEN</div>
    </div>
  </section>

  <section class="card card--back" aria-label="Business card back">
    <svg class="card-shapes" viewBox="0 0 435 262" preserveAspectRatio="none" aria-hidden="true">
      <rect class="shape-band" x="0" y="238" width="300" height="10"/>
      <polygon class="shape-plum" points="432,0 435,0 435,262 275,262"/>
    </svg>
    <div class="brand">
      <div class="brand-dot"></div>
      <div class="brand-name">GOWNHAVEN</div>
    </div>

    <div class="holder">
      <div class="holder-name">MARCO VILLALTA</div>
      <div class="holder-role">DIRECTOR</div>
    </div>

    <ul class="contact-list">
      <li class="contact-item">
        <svg class="contact-icon" viewBox="0 0 16 16" aria-hidden="true"><path d="M4 1h5a1 1 0 0 1 1 1v12a1 1 0 0 1-1 1H4a1 1 0 0 1-1-1V2a1 1 0 0 1 1-1zm1 2v8h3V3z"/></svg>
        <span>(555) 204-3180</span>
      </li>
      <li class="contact-item">
        <svg class="contact-icon" viewBox="0 0 16 16" aria-hidden="true"><path d="M1 3h14v10H1zm1.5 1.2L8 8.3l5.5-4.1z"/></svg>
        <span>Info@Gownhaven.com</span>
      </li>
      <li class="contact-item">
        <svg class="contact-icon" viewBox="0 0 16 16" aria-hidden="true"><path d="M8 1a7 7 0 1 0 0 14A7 7 0 0 0 8 1zm-1 2.2V7H3.1A5 5 0 0 1 7 3.2zm2 0A5 5 0 0 1 12.9 7H9zM3.1 9H7v3.8A5 5 0 0 1 3.1 9zM9 9h3.9A5 5 0 0 1 9 12.8z"/></svg>
        <span>www.gownhavenglam.com</span>
      </li>
      <li class="contact-item">
        <svg class="contact-icon" viewBox="0 0 16 16" aria-hidden="true"><path d="M8 1l7 6.5h-2V15H9.5v-4h-3v4H3V7.5H1z"/></svg>
        <span>48 Alameda Ave., Suite</span>
      </li>
    </ul>
  </section>

</main>
</body>
</html>
```